Harwick Legal

To update and modernize current business card appearance. Marta's business is based in Melbourne with 4 other lawyers in the firm. Marta travels to the Pilbara in Western Australia approximately 1 week a month as part of the firms legal work. She consults with clients in Newman, Tom Price and Port Hedland. The lawyers work mostly from a home office, apart from court appearances. They have a virtual office in Melbourne city, and use facilities in 3 or 4 other locations around Melbourne. It is important the client's think this is a conventional law firm with a permanent office. Our business structure is a difficult concept for them to grasp. The business has been operational for 3 years, growing from 1 lawyer to 4 lawyers during that time. Our website is www.Harwicklegal.example.au and is currently being upgraded as we are not happy with its content. The logo is currently orange and dark grey but the orange is a difficult colour to reproduce and often turns out "poo" brown when documents are printed. We need clients to know we are user friendly and caring - and not head up our rears ends as some lawyers appear to be.
Updates

Thank you for the feedback so far. 1. Some of the designs have too much black (We prefer darker grey & not too much.) 2. Happy for designers to play around with different colours & logo design. What we're after is a modern look and business card that people say "wow" when they pick it up.

Industry/Entity Type

Business

```html
<!DOCTYPE html>
<html lang="en">
<head>
<meta charset="utf-8">
<title>Harwick Legal – Business Card</title>
<link rel="stylesheet" href="https://fonts.googleapis.com/css2?family=Cinzel:wght@500&family=Michroma&display=swap">
<style>
  :root {
    --bg: #ecebe8;
    --frame-dark: #5d5f63;
    --frame-light: #d9dadc;
    --paper: #ffffff;
    --ink: #3a3d42;
    --ink-soft: #55585d;
    --accent: #1c7c8c;
    --band: #3a3d42;
    --band-text: #ffffff;
    --rule: #a4a6a9;
  }
  html, body {
    margin: 0;
    width: 1200px;
    height: 677px;
    overflow: hidden;
    background: var(--bg);
  }
  .stage {
    width: 1200px;
    height: 677px;
    display: flex;
    align-items: center;
    justify-content: center;
  }
  .card {
    width: 340px;
    height: 590px;
    box-sizing: border-box;
    padding: 9px;
    background: linear-gradient(135deg, var(--frame-dark), var(--frame-light) 45%, var(--frame-dark) 100%);
    box-shadow: 0 10px 28px rgba(0,0,0,.18);
  }
  .card-face {
    position: relative;
    height: 100%;
    background: var(--paper);
    display: flex;
    flex-direction: column;
  }
  .brand {
    padding: 44px 0 28px;
    display: flex;
    flex-direction: column;
    align-items: center;
  }
  .brand-mark {
    width: 66px;
    height: 66px;
    border: 3px solid var(--accent);
    border-radius: 50%;
    box-sizing: border-box;
    margin-bottom: 16px;
  }
  .brand-name {
    font-family: "Cinzel", serif;
    font-weight: 500;
    font-size: 28px;
    letter-spacing: 1px;
    color: var(--ink);
    margin: 0;
    padding-bottom: 8px;
    border-bottom: 1px solid var(--ink);
  }
  .name-band {
    background: var(--band);
    color: var(--band-text);
    font-family: "Michroma", sans-serif;
    text-align: right;
    padding: 18px 26px 18px 20px;
  }
  .person-name { font-size: 16px; letter-spacing: 1px; margin: 0 0 6px; }
  .person-role { font-size: 11.5px; letter-spacing: 1px; margin: 0; }
  .contacts {
    list-style: none;
    margin: 0;
    padding: 34px 24px 0;
    font-family: "Michroma", sans-serif;
    font-size: 10px;
    color: var(--ink-soft);
  }
  .contact-item {
    display: flex;
    align-items: center;
    gap: 12px;
    margin-bottom: 15px;
  }
  .contact-icon {
    width: 20px;
    height: 20px;
    background: var(--accent);
    display: flex;
    align-items: center;
    justify-content: center;
    flex: none;
  }
  .contact-icon svg { width: 13px; height: 13px; fill: #fff; }
  .contact-address {
    margin-top: 22px;
    padding-top: 16px;
    border-top: 1px solid var(--rule);
  }
  .foot-rule {
    position: absolute;
    left: 24px;
    right: 24px;
    bottom: 30px;
    border-top: 1px solid var(--rule);
  }
</style>
</head>
<body>
<main class="stage">
  <article class="card">
    <div class="card-face">
      <header class="brand">
        <span class="brand-mark"></span>
        <h1 class="brand-name">Harwick Legal</h1>
      </header>

      <section class="name-band">
        <p class="person-name">OWEN PRYCE</p>
        <p class="person-role">GENERAL MANAGER</p>
      </section>

      <ul class="contacts">
        <li class="contact-item">
          <span class="contact-icon"><svg viewBox="0 0 24 24"><path d="M6.6 10.8a15.1 15.1 0 0 0 6.6 6.6l2.2-2.2c.3-.3.7-.4 1-.2 1.1.4 2.3.6 3.6.6.6 0 1 .4 1 1V20c0 .6-.4 1-1 1A17 17 0 0 1 3 4c0-.6.4-1 1-1h3.5c.6 0 1 .4 1 1 0 1.3.2 2.5.6 3.6.1.3 0 .7-.2 1z"/></svg></span>
          014 220 5318
        </li>
        <li class="contact-item">
          <span class="contact-icon"><svg viewBox="0 0 24 24"><path d="M6 2h12v20H6zM8 4v14h8V4zm3 15h2v1h-2z"/></svg></span>
          014 220 5319
        </li>
        <li class="contact-item">
          <span class="contact-icon"><svg viewBox="0 0 24 24"><path d="M2 5h20v14H2zm2 2v.5l8 5 8-5V7zm0 2.8V17h16V9.8l-8 5z"/></svg></span>
          owen@harwicklegal.example.au
        </li>
        <li class="contact-item">
          <span class="contact-icon"><svg viewBox="0 0 24 24"><path d="M12 2a10 10 0 1 0 0 20 10 10 0 0 0 0-20zm0 2c.9 1.2 1.6 2.7 2 4.5h-4c.4-1.8 1.1-3.3 2-4.5zM4.3 14a8 8 0 0 1 0-4h3.4a16 16 0 0 0 0 4zm.8 2h3c.3 1.3.8 2.6 1.5 3.6A8 8 0 0 1 5.1 16zm3-8h-3a8 8 0 0 1 4.5-3.6C8.9 5.4 8.4 6.7 8.1 8zM12 20c-.9-1.2-1.6-2.7-2-4h4c-.4 1.3-1.1 2.8-2 4zm2.3-6H9.7a14 14 0 0 1 0-4h4.6a14 14 0 0 1 0 4zm.1 5.6c.7-1 1.2-2.3 1.5-3.6h3a8 8 0 0 1-4.5 3.6zM16.3 14a16 16 0 0 0 0-4h3.4a8 8 0 0 1 0 4zm-.4-6c-.3-1.3-.8-2.6-1.5-3.6A8 8 0 0 1 18.9 8z"/></svg></span>
          www.Harwicklegal.example.au
        </li>
        <li class="contact-item contact-address">
          <span class="contact-icon"><svg viewBox="0 0 24 24"><path d="M12 2a7 7 0 0 0-7 7c0 5.2 7 13 7 13s7-7.8 7-13a7 7 0 0 0-7-7zm0 9.5a2.5 2.5 0 1 1 0-5 2.5 2.5 0 0 1 0 5z"/></svg></span>
          Level 9, 41 Collins Street Melbourne
        </li>
      </ul>
      <div class="foot-rule"></div>
    </div>
  </article>
</main>
</body>
</html>
```